Website Design For digital agency

We have an existing website called www.qlmr.co.uk which needs revamping. We are currently using the Duda web builder platform to build our website so we need someone to create or combine our existing pages into a user friends, modern design. We will need design assets for our internal team to implement. Here is a link to our support if you have any question regarding the the website builder or image sizes and available design widgets. https://help.pagevantor.com/hc/en-us/articles/480027155302-Image-Size-Guidelines

Target Market(s)

Small to medium businesses looking for revamps and new designs

Industry/Entity Type

Website

Number of Pages Required

5+ page

Other font styles liked:
• Publica

Colors
33a6d7
3377b5
886aae

Requirements
Must have
• separate pages to outline the services we provide.

```html
<!DOCTYPE html>
<html lang="en">
<head>
<meta charset="utf-8">
<title>Brightlane — Digital Agency</title>
<link href="https://fonts.googleapis.com/css2?family=Comfortaa:wght@500;700&family=Montserrat:wght@400;500;600;700;800&display=swap" rel="stylesheet">
<style>
:root{
  --purple:#8e3a9b;
  --navy:#1d3b7a;
  --deep:#1a4a88;
  --teal:#33a6d7;
  --grey-bg:#f6f6f8;
  --text:#555a66;
  --muted:#7a7f8a;
  --white:#ffffff;
  --grad:linear-gradient(90deg,var(--purple),var(--navy));
}
*{margin:0;padding:0;box-sizing:border-box}
html,body{width:1200px;height:3827px;overflow:hidden}
body{position:relative;background:var(--white);font-family:"Montserrat",sans-serif;color:var(--text)}
.abs{position:absolute}

/* top bar + nav */
.topbar{left:0;top:0;width:1200px;height:37px;background:var(--purple)}
.topbar .dot{position:absolute;top:12px;width:13px;height:13px;border:2px solid var(--white);border-radius:50%}
.nav{left:0;top:37px;width:1200px;height:64px;background:var(--white)}
.brand{display:flex;align-items:center;gap:10px;font-family:"Comfortaa",sans-serif;font-weight:700;font-size:30px;color:var(--navy);white-space:nowrap}
.brand .mark{width:34px;height:34px;border-radius:50%;background:var(--purple)}
.nav-brand{position:absolute;left:71px;top:12px}
.nav-link{position:absolute;top:24px;font-size:12.5px;color:var(--muted)}
.nav-link.active{color:var(--navy);font-weight:500}
.nav-underline{left:629px;top:97px;width:42px;height:3px;background:var(--navy)}
.btn{position:absolute;display:flex;align-items:center;justify-content:center;color:var(--white);font-weight:600;font-size:13px;letter-spacing:-.3px;border-radius:6px}
.btn-navy{background:var(--navy)}
.btn-grad{background:var(--grad)}
.btn-purple{background:var(--purple)}

/* hero */
.hero{left:0;top:101px;width:1200px;height:671px;background:linear-gradient(120deg,#5a6470 0%,#8a8e92 45%,#c9c4bd 75%,#e6e3de 100%)}
.hero-curve{left:0;top:101px}
.hero-title{left:62px;top:262px;font-family:"Comfortaa",sans-serif;font-weight:700;font-size:52px;line-height:60px;color:var(--white)}
.hero-lead{left:62px;top:425px;font-size:16px;font-weight:500;color:var(--white)}

/* section titles */
.sec-title{font-family:"Montserrat",sans-serif;font-weight:700;font-size:27px;color:var(--navy);letter-spacing:.3px}
.sec-title span{color:var(--purple)}

/* services cards */
.services-bg{left:0;top:700px;width:1200px;height:660px;background:var(--grey-bg)}
.card{position:absolute;top:919px;width:232px;height:262px;background:var(--white);border-radius:8px;box-shadow:0 4px 18px rgba(30,40,90,.08);text-align:center}
.card.featured{background:linear-gradient(135deg,var(--purple),var(--navy))}
.card svg.icon{position:absolute;left:84px;top:30px}
.card h3{position:absolute;left:0;width:100%;top:122px;font-family:"Comfortaa",sans-serif;font-weight:700;font-size:15.5px;color:#222}
.card .sub{position:absolute;left:0;width:100%;top:155px;font-size:13px;color:var(--purple)}
.card p{position:absolute;left:20px;width:192px;top:178px;font-size:11.5px;line-height:19.5px;color:var(--muted)}
.card.featured h3,.card.featured p{color:var(--white)}
.card.featured .sub{color:var(--teal)}
.card .go{position:absolute;left:98px;top:244px;width:36px;height:36px;border-radius:50%;background:var(--purple);display:flex;align-items:center;justify-content:center}
.card.featured .go{background:var(--white)}
.slider-arrow{top:1035px}

/* about services */
.about-text{left:162px;width:390px;font-size:11.6px;line-height:19.5px;color:var(--muted)}
.blob{left:655px;top:1381px}

/* login band */
.login-band{left:0;top:1844px}
.screen{left:146px;top:1920px;width:386px;height:210px;border-radius:8px;background:#2c2f36;padding:10px}
.screen .view{width:366px;height:182px;background:linear-gradient(120deg,#6e7680,#b9b5ae);border-radius:2px}
.screen-chin{left:146px;top:2130px;width:386px;height:34px;background:#d9dadd;border-radius:0 0 8px 8px}
.screen-stand{left:296px;top:2164px;width:86px;height:38px;background:linear-gradient(#cfd1d4,#b5b8bc)}
.login-title{left:655px;top:1980px;font-family:"Comfortaa",sans-serif;font-weight:700;font-size:28px;color:var(--white)}
.radio{position:absolute;top:2039px;width:12px;height:12px;border-radius:50%;border:1.5px solid var(--white)}
.radio.on{background:var(--white)}
.radio-label{position:absolute;top:2036px;font-family:"Comfortaa",sans-serif;font-weight:700;font-size:14px;color:var(--white);letter-spacing:.5px}
.btn-white{background:var(--white);color:var(--navy)}

/* blog */
.post-img{position:absolute;top:2348px;width:300px;height:337px;border-radius:6px}
.post-meta{position:absolute;top:2668px;width:190px;height:32px;background:var(--white);border-radius:6px;display:flex;align-items:center;justify-content:center;gap:20px;font-size:11.5px;color:var(--purple)}
.post-meta span{display:flex;align-items:center;gap:5px}
.post-title{position:absolute;top:2715px;width:300px;text-align:center;font-family:"Comfortaa",sans-serif;font-weight:700;font-size:14px;line-height:24px;color:#222}
.read-more{position:absolute;top:2774px;width:300px;text-align:center;font-family:"Comfortaa",sans-serif;font-weight:700;font-size:11.5px;color:var(--navy)}

/* contact */
.contact-bg{left:0;top:2910px}
.person{left:59px;top:2829px;width:498px;height:598px;border-radius:250px 250px 0 0;background:linear-gradient(180deg,#c9b9a8 0%,#5b86bd 30%,#2c4a7c 100%)}
.contact-title{left:646px;top:2997px;font-size:28px}
.contact-lead{left:646px;top:3040px;font-family:"Comfortaa",sans-serif;font-weight:700;font-size:21px;line-height:31px;color:#222}
.field{position:absolute;left:645px;width:337px;background:var(--white);border:1px solid #d7d8dc;border-radius:3px;padding:10px 9px;font-size:11.5px;color:var(--muted)}

/* footer */
.footer{left:0;top:3427px;width:1200px;height:357px;background:linear-gradient(100deg,var(--purple) 0%,#52378a 55%,var(--navy) 100%)}
.foot-brand{position:absolute;left:59px;top:3525px;color:var(--white)}
.foot-brand .mark{background:var(--white)}
.foot-text{left:61px;top:3580px;width:250px;font-size:11.6px;line-height:20px;color:var(--white)}
.foot-social{position:absolute;top:3670px;width:34px;height:34px;border-radius:50%;border:2px solid var(--white)}
.foot-social.filled{background:var(--white)}
.foot-head{position:absolute;top:3503px;font-family:"Comfortaa",sans-serif;font-weight:700;font-size:17.5px;line-height:24px;color:var(--white)}
.foot-link{position:absolute;left:339px;font-size:12px;color:var(--white)}
.foot-link::before{content:"";display:inline-block;width:5px;height:5px;border:1px solid var(--white);transform:rotate(45deg);margin-right:8px;vertical-align:2px}
.foot-contact{position:absolute;left:613px;display:flex;gap:14px;align-items:flex-start;font-size:12px;line-height:19px;color:var(--white)}
.foot-contact svg{flex:none}
.foot-input{left:887px;top:3568px;width:252px;height:33px;background:var(--white);border-radius:2px;padding:9px 12px;font-size:12px;color:#444}
.copyright{left:0;top:3784px;width:1200px;height:43px;background:var(--deep);color:var(--white);font-size:11.5px;display:flex;align-items:center;justify-content:center}
</style>
</head>
<body>

<!-- header -->
<div class="abs topbar">
  <span class="dot" style="left:1094px"></span>
  <span class="dot" style="left:1125px;border-radius:3px"></span>
</div>
<header class="abs nav">
  <div class="brand nav-brand"><span class="mark"></span>Brightlane</div>
  <a class="nav-link active" style="left:626px">Home</a>
  <a class="nav-link" style="left:701px">About Us</a>
  <a class="nav-link" style="left:796px">Services</a>
  <a class="nav-link" style="left:886px">Blog</a>
  <a class="nav-link" style="left:957px">Login</a>
  <a class="btn btn-navy" style="left:1020px;top:15px;width:119px;height:36px">CONTACT US</a>
</header>
<div class="abs nav-underline"></div>

<!-- hero -->
<section class="abs hero" role="img" aria-label="Photo of a developer working at a computer in a bright office"></section>
<svg class="abs hero-curve" width="1200" height="671" viewBox="0 0 1200 671" aria-hidden="true">
  <path d="M0 609 Q600 733 1200 609 L1200 671 L0 671 Z" fill="#f6f6f8"/>
</svg>
<h1 class="abs hero-title">Let us help you<br>grow your business!</h1>
<p class="abs hero-lead">Making your Business better is our priority.</p>
<a class="btn btn-purple" style="left:59px;top:493px;width:134px;height:37px">GET A QUOTE</a>

<!-- services slider -->
<div class="abs services-bg"></div>
<h2 class="abs sec-title" style="left:0;width:1200px;text-align:center;top:858px"><span>SOME OF</span> OUR SERVICES</h2>

<svg class="abs slider-arrow" style="left:66px" width="16" height="26" viewBox="0 0 16 26"><path d="M13 2 L3 13 L13 24" fill="none" stroke="#1d3b7a" stroke-width="2"/></svg>
<svg class="abs slider-arrow" style="left:1116px" width="16" height="26" viewBox="0 0 16 26"><path d="M3 2 L13 13 L3 24" fill="none" stroke="#1d3b7a" stroke-width="2"/></svg>

<div class="card" style="left:99px">
  <svg class="icon" width="64" height="62" viewBox="0 0 64 62" fill="none" stroke="#1d3b7a" stroke-width="2"><rect x="4" y="4" width="24" height="20" rx="2"/><rect x="36" y="4" width="24" height="20" rx="2" stroke="#8e3a9b"/><rect x="4" y="32" width="24" height="24" rx="2" stroke="#8e3a9b"/><rect x="36" y="32" width="24" height="24" rx="2"/><path d="M10 12h12M42 12h12M42 44h12"/></svg>
  <h3>Social Media</h3><div class="sub">Marketing</div>
  <p>Reach thousands of potential new customers online</p>
  <span class="go"><svg width="10" height="14" viewBox="0 0 10 14"><path d="M2 1l6 6-6 6" fill="none" stroke="#fff" stroke-width="2"/></svg></span>
</div>
<div class="card featured" style="left:355px">
  <svg class="icon" width="64" height="62" viewBox="0 0 64 62" fill="none" stroke="#fff" stroke-width="2"><path d="M12 4h34v40H12z"/><path d="M18 14h22M18 22h22M18 30h12"/><rect x="34" y="28" width="18" height="14"/><path d="M6 44l14 14M50 44l8 8"/></svg>
  <h3>Press Release</h3><div class="sub">Content distribution</div>
  <p>great way to put your products and services on display</p>
  <span class="go"><svg width="10" height="14" viewBox="0 0 10 14"><path d="M2 1l6 6-6 6" fill="none" stroke="#8e3a9b" stroke-width="2"/></svg></span>
</div>
<div class="card" style="left:609px">
  <svg class="icon" width="64" height="62" viewBox="0 0 64 62" fill="none" stroke="#1d3b7a" stroke-width="2"><rect x="14" y="2" width="36" height="54" rx="3"/><circle cx="32" cy="20" r="8" stroke="#8e3a9b"/><path d="M22 44v-8M30 44v-12M38 44v-6M4 40l10 10M60 40l-10 10"/></svg>
  <h3>SEO</h3><div class="sub">Management</div>
  <p>Every managed SEO plan is custom to fit your needs</p>
  <span class="go"><svg width="10" height="14" viewBox="0 0 10 14"><path d="M2 1l6 6-6 6" fill="none" stroke="#fff" stroke-width="2"/></svg></span>
</div>
<div class="card" style="left:864px">
  <svg class="icon" width="64" height="62" viewBox="0 0 64 62" fill="none" stroke="#1d3b7a" stroke-width="2"><rect x="8" y="20" width="48" height="30" rx="2"/><path d="M2 54h60"/><circle cx="32" cy="12" r="8" stroke="#8e3a9b"/><path d="M32 20v14M24 40h16" stroke="#8e3a9b"/></svg>
  <h3>Blog writing</h3><div class="sub">Content management</div>
  <p>high quality content direct to your site each month.</p>
  <span class="go"><svg width="10" height="14" viewBox="0 0 10 14"><path d="M2 1l6 6-6 6" fill="none" stroke="#fff" stroke-width="2"/></svg></span>
</div>

<!-- about services -->
<svg class="abs" style="left:0;top:1204px" width="1200" height="146" viewBox="0 0 1200 146" aria-hidden="true"><path d="M0 146 Q600 0 1200 146 Z" fill="#fff"/></svg>
<div class="abs" style="left:0;top:1349px;width:1200px;height:860px;background:#fff"></div>
<h2 class="abs sec-title" style="left:159px;top:1392px"><span>SOME OF</span> OUR SERVICES</h2>
<p class="abs about-text" style="top:1450px">We provide small to medium sized businesses with a full range of Web Services including high quality Custom Website Design, Website Development and Search Marketing services. Our clients range from small start-up businesses, to sizeable, brand recognisable organisations. Whatever your business, we will help it to perform better just like we've done for our clients.</p>
<p class="abs about-text" style="top:1577px">We set our prices at extremely competitive levels and offer unlimited design revisions with all websites we create, thus providing our clients with 100% satisfaction guaranteed. We truly believe that we have got the quality/price balance spot on. We are the right choice if you're looking for an affordable website that will turn visitors in to customers.</p>
<a class="btn btn-grad" style="left:161px;top:1718px;width:157px;height:36px">VIEW OUR WORK</a>

<svg class="abs" style="left:662px;top:1380px" width="42" height="46" viewBox="0 0 42 46" fill="none" stroke="#8e3a9b" stroke-width="2" aria-hidden="true"><path d="M21 2 L38 19 L21 36 L4 19 Z"/><path d="M17 10 L34 27 L17 44 L0 27 Z"/></svg>
<svg class="abs blob" width="485" height="380" viewBox="0 0 485 380" role="img" aria-label="Photo of hands typing on a laptop showing analytics charts">
  <defs><linearGradient id="blobFill" x1="0" y1="0" x2="1" y2="1"><stop offset="0" stop-color="#9aa5b4"/><stop offset=".5" stop-color="#c8ccd8"/><stop offset="1" stop-color="#7d8796"/></linearGradient></defs>
  <path d="M20 60 C40 10 110 -4 170 20 C220 40 250 50 300 50 C380 48 470 80 482 150 C492 220 440 250 410 300 C380 360 320 390 260 370 C210 355 170 330 120 330 C60 330 10 290 6 220 C2 160 4 100 20 60 Z" fill="url(#blobFill)"/>
</svg>

<!-- login band -->
<svg class="abs login-band" width="1200" height="357" viewBox="0 0 1200 357" aria-hidden="true">
  <defs><linearGradient id="bandFill" x1="0" x2="1"><stop offset="0" stop-color="#8e3a9b"/><stop offset=".55" stop-color="#5a3a8e"/><stop offset="1" stop-color="#1d3b7a"/></linearGradient></defs>
  <path d="M0 71 Q600 -71 1200 71 L1200 357 L0 357 Z" fill="url(#bandFill)"/>
</svg>
<div class="abs screen" role="img" aria-label="Desktop monitor showing the website homepage"><div class="view"></div></div>
<div class="abs screen-chin"></div>
<div class="abs screen-stand"></div>
<div class="abs login-title">Login</div>
<span class="radio on" style="left:652px"></span><span class="radio-label" style="left:687px">WEBSITE LOGIN</span>
<span class="radio" style="left:848px"></span><span class="radio-label" style="left:882px">DOMAIN &amp; EMAIL LOGIN</span>
<a class="btn btn-white" style="left:652px;top:2094px;width:98px;height:37px">LOGIN</a>

<!-- blog -->
<h2 class="abs sec-title" style="left:0;width:1200px;text-align:center;top:2282px"><span>OUR</span> BLOG</h2>

<div class="post-img" style="left:120px;background:linear-gradient(160deg,#d8d4cf,#8c8f96)" role="img" aria-label="Photo of hands typing on a laptop"></div>
<div class="post-img" style="left:450px;background:linear-gradient(160deg,#e8e1d8,#b9a896)" role="img" aria-label="Photo of a woman looking at her phone beside a laptop"></div>
<div class="post-img" style="left:780px;background:linear-gradient(160deg,#c9b59c,#6d6a72)" role="img" aria-label="Photo of a team gathered around a laptop"></div>

<div class="post-meta" style="left:175px">
  <span><svg width="12" height="12" viewBox="0 0 12 12" fill="none" stroke="#8e3a9b"><rect x="1" y="2" width="10" height="9"/><path d="M1 5h10M4 0v3M8 0v3"/></svg>25 May</span>
  <span><svg width="10" height="12" viewBox="0 0 10 12" fill="none" stroke="#8e3a9b"><path d="M7 3v6a2 2 0 0 1-4 0V2a1.5 1.5 0 0 1 3 0v6"/></svg>Design</span>
</div>
<div class="post-meta" style="left:505px">
  <span><svg width="12" height="12" viewBox="0 0 12 12" fill="none" stroke="#8e3a9b"><rect x="1" y="2" width="10" height="9"/><path d="M1 5h10M4 0v3M8 0v3"/></svg>25 May</span>
  <span><svg width="10" height="12" viewBox="0 0 10 12" fill="none" stroke="#8e3a9b"><path d="M7 3v6a2 2 0 0 1-4 0V2a1.5 1.5 0 0 1 3 0v6"/></svg>Design</span>
</div>
<div class="post-meta" style="left:835px">
  <span><svg width="12" height="12" viewBox="0 0 12 12" fill="none" stroke="#8e3a9b"><rect x="1" y="2" width="10" height="9"/><path d="M1 5h10M4 0v3M8 0v3"/></svg>25 May</span>
  <span><svg width="10" height="12" viewBox="0 0 10 12" fill="none" stroke="#8e3a9b"><path d="M7 3v6a2 2 0 0 1-4 0V2a1.5 1.5 0 0 1 3 0v6"/></svg>Design</span>
</div>

<h3 class="post-title" style="left:120px">The 3 Most Important Steps to<br>Solving Low Conversion</h3>
<h3 class="post-title" style="left:450px">10 Clever Marketing Ideas to<br>Grow Sales During a Festival</h3>
<h3 class="post-title" style="left:780px">How to Promote Your Business<br>to Festival Attendees</h3>
<a class="read-more" style="left:120px">READ MORE ›</a>
<a class="read-more" style="left:450px">READ MORE ›</a>
<a class="read-more" style="left:780px">READ MORE ›</a>

<!-- contact -->
<svg class="abs contact-bg" width="1200" height="517" viewBox="0 0 1200 517" aria-hidden="true"><path d="M0 67 Q600 -30 1200 67 L1200 517 L0 517 Z" fill="#f6f6f8"/></svg>
<div class="abs person" role="img" aria-label="Photo of a smiling businessman holding a tablet"></div>
<h2 class="abs sec-title contact-title"><span>CONTACT</span> US</h2>
<p class="abs contact-lead">Need to improve the look of your<br>project or your business?</p>
<div class="field" style="top:3124px;height:35px">Name:</div>
<div class="field" style="top:3169px;height:36px">Email:</div>
<div class="field" style="top:3214px;height:59px">Message:</div>
<a class="btn btn-grad" style="left:645px;top:3297px;width:135px;height:37px">SUBMIT NOW</a>

<!-- footer -->
<footer class="abs footer"></footer>
<div class="brand foot-brand"><span class="mark"></span>Brightlane</div>
<p class="abs foot-text">Every campaign we launch starts with a dream - your dream. And the first thing we do to discover that dream is listen to you.</p>
<span class="foot-social filled" style="left:59px"></span>
<span class="foot-social" style="left:105px"></span>

<h4 class="foot-head" style="left:339px">About Us</h4>
<a class="foot-link" style="top:3547px">Home</a>
<a class="foot-link" style="top:3577px">About Us</a>
<a class="foot-link" style="top:3607px">Services</a>
<a class="foot-link" style="top:3637px">Blog</a>
<a class="foot-link" style="top:3667px">Login</a>
<a class="foot-link" style="top:3697px">Contact Us</a>

<h4 class="foot-head" style="left:613px">Contact Us</h4>
<div class="foot-contact" style="top:3545px">
  <svg width="14" height="22" viewBox="0 0 14 22" fill="none" stroke="#fff" stroke-width="1.6"><rect x="1" y="1" width="12" height="20" rx="2"/><path d="M5 17h4"/></svg>
  <span>48 Alder Lane, Wexbury,<br>WX4 2PL, United Kingdom</span>
</div>
<div class="foot-contact" style="top:3606px">
  <svg width="20" height="20" viewBox="0 0 20 20" fill="none" stroke="#fff" stroke-width="1.6"><path d="M4 2l4 4-2 3c1 2 3 4 5 5l3-2 4 4-3 3C9 19 1 11 1 5z"/></svg>
  <span>+44 7000 123456</span>
</div>
<div class="foot-contact" style="top:3651px">
  <svg width="20" height="16" viewBox="0 0 20 16" fill="none" stroke="#fff" stroke-width="1.6"><rect x="1" y="1" width="18" height="14"/><path d="M1 1l9 8 9-8"/></svg>
  <span>hello@brightlane.example</span>
</div>
<div class="foot-contact" style="top:3695px">
  <svg width="20" height="20" viewBox="0 0 20 20" fill="none" stroke="#fff" stroke-width="1.6"><circle cx="10" cy="10" r="9"/><ellipse cx="10" cy="10" rx="4" ry="9"/><path d="M1 10h18"/></svg>
  <span>www.brightlane.example</span>
</div>

<h4 class="foot-head" style="left:888px">Sign Up For A<br>Newsletters</h4>
<div class="abs foot-input">Enter Email Add.....</div>
<a class="btn btn-purple" style="left:888px;top:3617px;width:134px;height:35px">SUBSRIBE NOW</a>

<div class="abs copyright">© Copyright 2021 Harbor Kin-All Right Reserved.</div>

</body>
</html>
```